Flyer Tally Desk Ledger Kit

Hi
Can you please design me a DL Flyer for: Tally Desk Ledger Kit
Info:
Starting a new Business ?
Want to save on bookkeeping fees for your existing business?

You can now save 1000's off bookkeeping fees by Doing it Yourself.

Using our Bookkeeper software you simply key in the information as you go.

We offer one on one training, backup and support.
We can assist you with BAS Preparation and Payrol Advice.

Add Modules as required:
Point of Sale Module
Jobs Management Module
Website Intergration Module

Fee set up assistance and training.

Lets get the ball rolling: 1300 462 815
www.tldlk.com.au
admin@tldlk.com.au (use the logo thing you made)

Target Market(s)

Small Business

Colors
ec1f27
f04a50
f59296
fcdcdc
ffffff

Requirements
Nice to have
• image/s related to bookkeeping

```html
<!DOCTYPE html>
<html lang="en">
<head>
<meta charset="utf-8">
<title>Tally Desk Ledger Kit – DL Flyer</title>
<link href="https://fonts.googleapis.com/css2?family=Montserrat:wght@300;400;500;600;700;800;900&display=swap" rel="stylesheet">
<style>
  :root{
    --red:#ec1f27;
    --red-soft:#f04a50;
    --pink:#f59296;
    --blush:#fcdcdc;
    --white:#ffffff;
    --ink:#4a4a4a;
    --charcoal:#505050;
    --stage:#b3b1b3;
    --photo-warm:#8a7a68;
    --photo-dark:#3a3d45;
  }
  *{margin:0;padding:0;box-sizing:border-box}
  html,body{width:1200px;height:1097px;overflow:hidden;background:var(--stage);font-family:'Montserrat',sans-serif;color:var(--ink)}
  .stage{position:relative;width:1200px;height:1097px}
  .flyer{position:absolute;top:83px;width:445px;height:890px;background:linear-gradient(180deg,#f6f6f6,#ffffff 40%,#f3f3f3);box-shadow:4px 5px 8px rgba(0,0,0,.25);overflow:hidden}
  .flyer--front{left:114px}
  .flyer--back{left:618px}
  .flyer__art{position:absolute;left:0;top:0}
  .brand{position:absolute;font-weight:700;color:var(--red);letter-spacing:-.5px;display:flex;align-items:center;gap:10px}
  .brand__dot{width:14px;height:14px;border-radius:50%;background:var(--red)}
  .flyer--front .brand{left:0;right:0;top:46px;justify-content:center;font-size:30px}
  .flyer--back .brand{right:18px;top:30px;font-size:19px;background:rgba(255,255,255,.85);padding:6px 10px;border-radius:4px}
  .headline{position:absolute;left:37px;top:515px;font-weight:900;color:var(--red);font-size:35px;line-height:46px;letter-spacing:.5px}
  .question{position:absolute;left:37px;top:606px;font-size:24px;line-height:31px;font-weight:400}
  .question b{font-weight:700}
  .offer{position:absolute;left:37px;top:720px;font-size:17.5px;line-height:26px;font-weight:400}
  .offer b{color:var(--red);font-weight:700}
  .footer{position:absolute;left:0;right:0;bottom:0;height:75px;background:var(--charcoal);color:var(--white);text-align:center}
  .footer__rule{position:absolute;left:0;right:0;top:809px;height:1.5px;background:var(--red)}
  .url-pill{position:absolute;left:94px;width:257px;top:797px;height:31px;border-radius:16px;background:var(--red);outline:1.5px solid var(--red);outline-offset:2px;color:var(--white);font-weight:700;font-size:20px;line-height:31px;text-align:center}
  .flyer--front .footer p{font-size:17px;margin-top:26px;font-weight:400}
  .flyer--back .footer p{font-size:17px;line-height:21px;font-weight:400}
  .flyer--back .footer p:first-child{margin-top:20px}
  .footer b{font-weight:700}
  .intro{position:absolute;left:30px;top:352px;font-size:16.5px;line-height:24px;font-weight:500}
  .benefits{position:absolute;left:28px;top:408px;list-style:none;font-size:17px;line-height:24px;font-weight:400}
  .benefits li{display:flex;gap:10px;margin-bottom:6px}
  .benefits svg{flex:none;margin-top:4px}
  .modules{position:absolute;left:24px;top:545px;width:392px;height:182px;border:1.5px solid var(--red);border-radius:12px}
  .modules__title{position:absolute;left:50%;top:-12px;transform:translateX(-50%);background:#f9f9f9;padding:0 8px;white-space:nowrap;color:var(--red);font-weight:700;font-size:17px}
  .module{position:absolute;top:27px;width:120px;text-align:center;color:var(--red);font-weight:600;font-size:14.5px;line-height:16px}
  .module__icon{display:block;margin:0 auto 10px}
  .setup{position:absolute;left:0;right:0;top:742px;text-align:center;font-size:17px;font-weight:400}
  .caption{position:absolute;top:1001px;width:445px;text-align:center;font-size:13px;color:#222}
  .side-label{position:absolute;font-size:13px;color:#222;transform:rotate(-90deg);transform-origin:left top}
</style>
</head>
<body>
<main class="stage">

  <!-- FRONT -->
  <section class="flyer flyer--front">
    <svg class="flyer__art" width="445" height="890" viewBox="0 0 445 890">
      <defs>
        <linearGradient id="deskPhoto" x1="0" y1="0" x2="1" y2="1">
          <stop offset="0" stop-color="#2f3340"/>
          <stop offset=".5" stop-color="#9a8a78"/>
          <stop offset="1" stop-color="#c9b8a2"/>
        </linearGradient>
        <linearGradient id="calcPhoto" x1="0" y1="0" x2="1" y2="1">
          <stop offset="0" stop-color="#b8aa98"/>
          <stop offset="1" stop-color="#3e414a"/>
        </linearGradient>
      </defs>
      <path d="M0 134H445V395C380 420 330 440 300 455 220 486 90 478 0 432Z" fill="url(#deskPhoto)" role="img" aria-label="Photo: businessman working on a laptop showing financial charts at a desk"/>
      <path d="M0 432C90 478 220 486 300 458L300 470C210 500 90 490 0 452Z" fill="var(--red)"/>
      <path d="M20 466C120 495 230 500 300 484L300 488C220 506 110 500 20 466Z" fill="var(--charcoal)"/>
      <path d="M400 430L445 410V425L410 440Z" fill="var(--charcoal)"/>
      <circle cx="352" cy="461" r="72" fill="url(#calcPhoto)" stroke="var(--red)" stroke-width="3" role="img" aria-label="Photo: hands using a calculator"/>
    </svg>
    <div class="brand"><span class="brand__dot"></span>Tally Desk Ledger Kit</div>
    <h1 class="headline">STARTING A<br>NEW BUSINESS ?</h1>
    <p class="question">Want to <b>Save on<br>Bookkeeping Fees</b> for<br>your existing business?</p>
    <p class="offer">You can now <b>Save 1000’s off</b><br>Bookkeeping fees by Doing it Yourself.</p>
    <div class="footer__rule"></div>
    <div class="footer"><p>Lets get the ball rolling: <b>1300 462 815</b></p></div>
    <div class="url-pill">www.tldlk.com.au</div>
  </section>
  <span class="side-label" style="left:572px;top:973px">FRONT</span>
  <p class="caption" style="left:114px">Design Concept Bookkeeper DL Flyer -01</p>

  <!-- BACK -->
  <section class="flyer flyer--back">
    <svg class="flyer__art" width="445" height="890" viewBox="0 0 445 890">
      <defs>
        <linearGradient id="meetingPhoto" x1="0" y1="0" x2="1" y2="1">
          <stop offset="0" stop-color="#262a36"/>
          <stop offset=".55" stop-color="#8a7c70"/>
          <stop offset="1" stop-color="#d8d4cc"/>
        </linearGradient>
      </defs>
      <path d="M0 0H445V258C330 290 220 300 140 295 80 292 30 285 0 272Z" fill="url(#meetingPhoto)" role="img" aria-label="Photo: business people reviewing documents with pens and a calculator"/>
      <path d="M0 272C60 300 140 318 230 320 330 321 400 300 445 285V290C400 310 330 328 230 326 140 326 60 312 0 290Z" fill="var(--charcoal)"/>
      <path d="M60 285C160 310 280 310 445 258V278C300 320 170 320 60 285Z" fill="var(--red)"/>
    </svg>
    <div class="brand"><span class="brand__dot"></span>Tally Desk Ledger Kit</div>
    <p class="intro">Using our Bookkeeper software<br>you simply key in the information as you go.</p>
    <ul class="benefits">
      <li><svg width="16" height="16" viewBox="0 0 16 16"><circle cx="8" cy="8" r="8" fill="var(--red)"/><path d="M4.5 8.2l2.4 2.3 4.6-4.8" fill="none" stroke="#fff" stroke-width="2"/></svg><span>We offer one on one training,<br>backup and support.</span></li>
      <li><svg width="16" height="16" viewBox="0 0 16 16"><circle cx="8" cy="8" r="8" fill="var(--red)"/><path d="M4.5 8.2l2.4 2.3 4.6-4.8" fill="none" stroke="#fff" stroke-width="2"/></svg><span>We can assist you with<br>BAS Preparation and Payrol Advice.</span></li>
    </ul>
    <div class="modules">
      <h2 class="modules__title">Add Modules as required</h2>
      <div class="module" style="left:5px">
        <svg class="module__icon" width="86" height="86" viewBox="0 0 86 86"><circle cx="43" cy="43" r="41" fill="#fff" stroke="#8a8a8a" stroke-width="3"/><rect x="21" y="24" width="40" height="30" rx="3" fill="none" stroke="#444" stroke-width="2.5"/><path d="M17 58H65" stroke="#444" stroke-width="2.5"/><text x="32" y="47" font-size="15" font-weight="700" fill="#444" font-family="Montserrat,sans-serif">$</text><path d="M42 32h14M42 38h14M42 44h10" stroke="#444" stroke-width="2"/></svg>
        Point of Sale<br>Module
      </div>
      <div class="module" style="left:136px">
        <svg class="module__icon" width="86" height="86" viewBox="0 0 86 86"><circle cx="43" cy="43" r="41" fill="#fff" stroke="#8a8a8a" stroke-width="3"/><rect x="25" y="20" width="34" height="44" rx="3" fill="none" stroke="#444" stroke-width="2.5"/><text x="30" y="31" font-size="8" font-weight="800" fill="#444" font-family="Montserrat,sans-serif">JOBS</text><path d="M30 38h24M30 45h24M30 52h16" stroke="#444" stroke-width="2"/><path d="M50 58l12-12" stroke="#444" stroke-width="3"/></svg>
        Jobs<br>Management<br>Module
      </div>
      <div class="module" style="left:268px">
        <svg class="module__icon" width="86" height="86" viewBox="0 0 86 86"><circle cx="43" cy="43" r="41" fill="#fff" stroke="#8a8a8a" stroke-width="3"/><g fill="none" stroke="#444" stroke-width="2.2"><circle cx="43" cy="43" r="17"/><ellipse cx="43" cy="43" rx="7" ry="17"/><path d="M26 43h34M29 34h28M29 52h28"/><circle cx="43" cy="43" r="24" stroke-dasharray="4 6"/></g></svg>
        Website<br>Intergration<br>Module
      </div>
    </div>
    <p class="setup">Fee set up assistance and training.</p>
    <div class="footer__rule"></div>
    <div class="footer"><p>Lets get the ball rolling: <b>1300 462 815</b></p><p>admin@tldlk.com.au</p></div>
    <div class="url-pill">www.tldlk.com.au</div>
  </section>
  <span class="side-label" style="left:1076px;top:973px">BACK</span>
  <p class="caption" style="left:618px">Design Concept Bookkeeper DL Flyer -01</p>

</main>
</body>
</html>
```